Natural Skincare Product Labels Design

We are looking for a designer to create elegant but quirky, functional product labels for our natural skincare range.
The labels must reflect our brand’s values of simplicity, luxury, and the natural, handmade essence of our products.
https://www.pictogrove.com/marvellaskincare
1. Key Details
Packaging Dimensions
Container Types: Transparent jars.
Sizes for Body Products:
Diameter: 64mm–68mm.
Heights: 80mm, 88mm, and 97mm (lid height: 15mm).
Sizes for Face Creams:
Diameter: 60mm.
Height: 50mm (lid height: 15mm).
Label Fit: For body products, ideally one label size to fit all jar sizes.
For the smaller face cream jars, a separate, tailored label is required.
2. Label Placement
Options include a wrapped-around label or a combination of wrapped-around and top-of-jar elements.
Transparent jars mean the label must leave space for the product to be visible (e.g., partial wrap or cutout areas).
3. Content Requirements
Product Name: Prominently displayed.
Ingredient List: Dedicated space required.
Disclaimer/Usage Instructions: Include space for this information.
4. Design Goals
Look & Feel: Simple, upmarket, and natural, with a handmade essence.
Logo Usage: Our logo is finalized and available in gold, black, and white variants. Use Josefin Bold font for the logo if adjustments are required.
Color Palette: Neutral tones (e.g., whites, blacks, golds) are preferred, with flexibility for subtle pops of color tied to each product’s main ingredient.
5. Imagery
Open to including images and colours (e.g., botanical illustrations) that highlight the main ingredient (e.g., coffee beans, turmeric root, or honeycomb). Also open to labels having a prominent colour to tie it in to the main ingredient.
Alternatively, no images can also work for a clean design.
6. Current Design Context
Our temporary design features gold leaf on top and a simple handmade side label. We’re seeking to elevate this to a more polished, cohesive design.
7. Product Line
- Body Products (Larger Jars)
Tolo Body Butter
Key Ingredients: Guarana & Cupuaçu butter (inspired by Brazil).
Note: “Tolo” is slang for “bum.”
Manuka Honey Body Butter
Key Ingredients: Manuka honey (from New Zealand) & Cupuaçu butter.
Coffee Body Scrub
Key Ingredients: Coffee and Demerara sugar.
Whipped Body Soap - Turmeric
Key Ingredients: Turmeric and Bentonite clay.
Whipped Body Soap - Banana
- Face Products (Smaller Jars)
Face Cream
Key Ingredients: Carrot Oil and Raspberry Oil.
Features natural UV protection.
Good Night Cream
Key Ingredients: Enriched with Magnesium.
Promotes relaxation and restful sleep.
8. Submission Guidelines
Flexibility: Design should allow for consistent branding across all products while accommodating the varying jar sizes and ingredient focus.
Material Considerations: Labels should complement the transparent jars and allow the product inside to remain partially visible.
Print Elements: Incorporating gold accents is a plus but should not overpower the design.
We’re excited to see your vision for a label that celebrates the natural beauty and high quality of our skincare range. Please include mockups to showcase the design in use, particularly on transparent jars of varying sizes.
women 20-50 years of age

```html
<!DOCTYPE html>
<html lang="en">
<head>
<meta charset="utf-8">
<title>Marvella Natural Skincare – Product Labels</title>
<link href="https://fonts.googleapis.com/css2?family=Josefin+Sans:wght@300;400;600&family=Montserrat:wght@400;500&display=swap" rel="stylesheet">
<style>
  :root {
    --paper: #ffffff;
    --label: #000000;
    --gold: #c6942f;
    --white: #ffffff;
    --honey: #c6942f;
    --guarana: #b01fe0;
    --coffee: #b0531f;
  }
  * { margin: 0; padding: 0; box-sizing: border-box; }
  html, body { width: 758px; height: 1200px; overflow: hidden; background: var(--paper); }
  .sheet { position: relative; width: 758px; height: 1200px; }

  /* front panels */
  .front {
    position: absolute; top: 114px; width: 173px; height: 172px;
    background: var(--label); color: var(--white); text-align: center;
    font-family: "Josefin Sans", sans-serif;
  }
  .front .brand { position: absolute; top: 62px; left: 0; right: 0; font-size: 14px; font-weight: 400; letter-spacing: 2.6px; color: var(--gold); }
  .front .tagline { position: absolute; top: 80px; left: 0; right: 0; font-size: 4.5px; letter-spacing: 1.3px; color: var(--gold); }
  .front .title { position: absolute; top: 93px; left: 0; right: 0; font-size: 15.5px; line-height: 16px; font-weight: 400; letter-spacing: .4px; }
  .front .rule { position: absolute; top: 129px; left: 0; right: 0; height: 2px; }
  .front .key { position: absolute; top: 139px; left: 0; right: 0; font-size: 8.5px; line-height: 11px; font-weight: 300; letter-spacing: .2px; }

  /* full labels */
  .label {
    position: absolute; left: 42px; width: 675px; height: 241px;
    background: var(--label); color: var(--white);
  }
  .label .face { position: absolute; left: 0; top: 0; width: 372px; height: 100%; text-align: center; font-family: "Josefin Sans", sans-serif; }
  .label .brand { position: absolute; top: 88px; left: 0; right: 0; font-size: 21px; letter-spacing: 4px; color: var(--gold); }
  .label .tagline { position: absolute; top: 114px; left: 0; right: 0; font-size: 7px; letter-spacing: 2px; color: var(--gold); }
  .label .title { position: absolute; top: 128px; left: 0; right: 0; font-size: 25px; line-height: 23px; font-weight: 600; letter-spacing: .8px; }
  .label .rule { position: absolute; top: 182px; left: 50px; width: 273px; height: 3px; }
  .label .key { position: absolute; top: 194px; left: 0; right: 0; font-size: 13px; line-height: 16px; font-weight: 300; letter-spacing: .6px; }

  .label .info { position: absolute; left: 380px; width: 242px; top: 28px; text-align: center; font-family: "Montserrat", sans-serif; font-size: 12.4px; line-height: 14px; }
  .label .info h3 { font-size: 12.4px; font-weight: 500; color: var(--gold); letter-spacing: .4px; line-height: 14px; }
  .label .info p { margin-bottom: 12px; }
  .label .info .gap { margin-bottom: 30px; }

  .label .marks { position: absolute; left: 382px; top: 178px; display: flex; align-items: center; gap: 9px; }
  .label .volume { font-family: "Montserrat", sans-serif; font-size: 10.5px; font-weight: 500; margin-right: 6px; letter-spacing: .3px; }
  .label .badge { width: 38px; height: 38px; border-radius: 50%; border: 2px solid var(--white); }

  .honey .rule { background: var(--honey); }
  .guarana .rule { background: var(--guarana); }
  .coffee .rule { background: var(--coffee); }
</style>
</head>
<body>
<main class="sheet">

  <section class="front honey" style="left:43px">
    <div class="brand">MARVELLA</div>
    <div class="tagline">NATURAL SKINCARE</div>
    <div class="title">MANUKA HONEY<br>BODY BUTTER</div>
    <div class="rule"></div>
    <div class="key">MANUKA HONEY<br>&amp; CUPUAÇU BUTTER</div>
  </section>

  <section class="front guarana" style="left:281px">
    <div class="brand">MARVELLA</div>
    <div class="tagline">NATURAL SKINCARE</div>
    <div class="title">TOLO<br>BODY BUTTER</div>
    <div class="rule"></div>
    <div class="key">GUARANA &amp;<br>CUPUAÇU BUTTER</div>
  </section>

  <section class="front coffee" style="left:530px">
    <div class="brand">MARVELLA</div>
    <div class="tagline">NATURAL SKINCARE</div>
    <div class="title">COFFEE<br>BODY SCRUB</div>
    <div class="rule"></div>
    <div class="key">COFFEE AND<br>DEMERARA SUGAR</div>
  </section>

  <section class="label honey" style="top:370px">
    <div class="face">
      <div class="brand">MARVELLA</div>
      <div class="tagline">NATURAL SKINCARE</div>
      <div class="title">MANUKA HONEY<br>BODY BUTTER</div>
      <div class="rule"></div>
      <div class="key">MANUKA HONEY<br>&amp; CUPUAÇU BUTTER</div>
    </div>
    <div class="info">
      <h3>INGREDIENTS:</h3>
      <p>Shea butter, cocoa butter, manuka honey, coconut oil, sweet almond oil, jojoba oil, beeswax, vitamin E oil, aloe vera gel, essential oils.</p>
      <h3>HOW TO USE:</h3>
      <p>Apply to dry skin, massage gently, and let it absorb</p>
    </div>
    <div class="marks">
      <span class="volume">200ML</span>
      <svg width="34" height="34" viewBox="0 0 34 34" aria-label="Use within 1 month of opening"><path d="M4 11 L28 4 M5 14 H29 V30 H5 Z" fill="none" stroke="#fff" stroke-width="2.2"/><text x="17" y="27" fill="#fff" font-family="Montserrat, sans-serif" font-size="7.5" font-weight="600" text-anchor="middle">1M</text></svg>
      <div class="badge"></div><div class="badge"></div><div class="badge"></div>
    </div>
  </section>

  <section class="label guarana" style="top:655px">
    <div class="face">
      <div class="brand">MARVELLA</div>
      <div class="tagline">NATURAL SKINCARE</div>
      <div class="title">TOLO<br>BODY BUTTER</div>
      <div class="rule"></div>
      <div class="key">GUARANA &amp;<br>CUPUAÇU BUTTER</div>
    </div>
    <div class="info">
      <h3>INGREDIENTS:</h3>
      <p>Shea butter, cocoa butter, cupuaçu butter, guarana extract, coconut oil, sweet almond oil, jojoba oil, bees-wax, vitamin E oil, essential oils</p>
      <h3>HOW TO USE:</h3>
      <p>Apply to dry skin, massage gently, and let it absorb</p>
    </div>
    <div class="marks">
      <span class="volume">200ML</span>
      <svg width="34" height="34" viewBox="0 0 34 34" aria-label="Use within 1 month of opening"><path d="M4 11 L28 4 M5 14 H29 V30 H5 Z" fill="none" stroke="#fff" stroke-width="2.2"/><text x="17" y="27" fill="#fff" font-family="Montserrat, sans-serif" font-size="7.5" font-weight="600" text-anchor="middle">1M</text></svg>
      <div class="badge"></div><div class="badge"></div><div class="badge"></div>
    </div>
  </section>

  <section class="label coffee" style="top:941px">
    <div class="face">
      <div class="brand">MARVELLA</div>
      <div class="tagline">NATURAL SKINCARE</div>
      <div class="title">COFFEE<br>BODY SCRUB</div>
      <div class="rule"></div>
      <div class="key">COFFEE AND<br>DEMERARA SUGAR</div>
    </div>
    <div class="info">
      <h3>INGREDIENTS:</h3>
      <p class="gap">Ground coffee, demerara sugar, co-conut oil, sweet almond oil, vitamin E oil, essential oils.</p>
      <h3>HOW TO USE:</h3>
      <p>Apply to wet skin, massage gently, rinse thoroughly.</p>
    </div>
    <div class="marks">
      <span class="volume">200ML</span>
      <svg width="34" height="34" viewBox="0 0 34 34" aria-label="Use within 1 month of opening"><path d="M4 11 L28 4 M5 14 H29 V30 H5 Z" fill="none" stroke="#fff" stroke-width="2.2"/><text x="17" y="27" fill="#fff" font-family="Montserrat, sans-serif" font-size="7.5" font-weight="600" text-anchor="middle">1M</text></svg>
      <div class="badge"></div><div class="badge"></div><div class="badge"></div>
    </div>
  </section>

</main>
</body>
</html>
```